KT Hollin's Brochure - Panelform Systems

Hello,
We have an example of very simple brochure (attached below). We would like you to make it better. More sophisticated. More professional looking. All of the info in the document needs to go in the brochure.
Please let me know if you can execute. I will be happy to send over photos, logos etc, once I know.

```html
<!DOCTYPE html>
<html lang="en">
<head>
<meta charset="utf-8">
<title>KT Hollin's Brochure – Panelform Systems</title>
<link rel="stylesheet" href="https://fonts.googleapis.com/css2?family=Bebas+Neue&family=Roboto:wght@400;500&family=Roboto+Mono:wght@600&display=swap">
<style>
  :root {
    --navy: #283a8e;
    --navy-deep: #1d2a78;
    --grey: #a7a9ac;
    --backdrop: #bfcdd9;
    --paper: #ffffff;
  }
  * { margin: 0; padding: 0; box-sizing: border-box; }
  html, body { width: 1200px; height: 1200px; overflow: hidden; background: var(--backdrop); }
  .spread-wrap {
    position: absolute; left: 40px; top: 206px;
    width: 800px; height: 563px;
    transform: scale(1.4); transform-origin: 0 0;
    background: var(--paper);
    box-shadow: 0 4px 14px rgba(40, 60, 90, .25);
    overflow: hidden;
    color: var(--navy);
  }
  .spread-art { position: absolute; inset: 0; width: 800px; height: 563px; }
  .fold { position: absolute; left: 399.5px; top: 0; width: 1px; height: 563px; background: rgba(0,0,0,.08); }
  .brand-name {
    position: absolute; left: 20px; top: 24px;
    font-family: "Roboto", sans-serif; font-weight: 500; font-size: 15px;
    color: var(--navy);
  }
  .brand-name::before {
    content: ""; display: inline-block; width: 9px; height: 9px;
    background: var(--navy); margin-right: 6px; vertical-align: 1px;
  }
  .display-title {
    position: absolute;
    font-family: "Bebas Neue", sans-serif; font-weight: 400;
    line-height: .92; letter-spacing: .5px; color: var(--navy);
  }
  .title-left { left: 18px; top: 78px; font-size: 33px; }
  .title-right { left: 420px; top: 12px; font-size: 32px; }
  .product-list {
    position: absolute; left: 18px; top: 146px;
    list-style: none;
    font-family: "Roboto", sans-serif; font-size: 13px; line-height: 19px;
  }
  .product-list li::before { content: "•"; margin-right: 5px; }
  .lead-copy {
    position: absolute; left: 18px; top: 278px; width: 205px;
    font-family: "Roboto", sans-serif; font-weight: 500; font-size: 15px; line-height: 19px;
  }
  .benefit-list {
    position: absolute; left: 18px; top: 385px; width: 205px;
    list-style: none;
    font-family: "Roboto", sans-serif; font-size: 10.5px; line-height: 15px;
  }
  .benefit-list li { padding-left: 13px; position: relative; }
  .benefit-list li::before { content: "•"; position: absolute; left: 2px; }
  .intro-copy {
    position: absolute; left: 422px; top: 81px; width: 168px;
    font-family: "Roboto Mono", monospace; font-weight: 600; font-size: 9.9px; line-height: 14.4px;
  }
  .feature-list {
    position: absolute; left: 422px; top: 233px; width: 132px;
    list-style: none;
    font-family: "Roboto", sans-serif; font-size: 11px; line-height: 14px;
  }
  .feature-list li { padding-left: 11px; position: relative; margin-bottom: 13px; }
  .feature-list li::before { content: "•"; position: absolute; left: 0; }
</style>
</head>
<body>
  <div class="spread-wrap">
    <svg class="spread-art" viewBox="0 0 800 563" xmlns="http://www.w3.org/2000/svg">
      <defs>
        <linearGradient id="glass-tower" x1="0" y1="0" x2="1" y2="1">
          <stop offset="0" stop-color="#9fc1e6"/>
          <stop offset=".55" stop-color="#6f8fb4"/>
          <stop offset="1" stop-color="#4b6a93"/>
        </linearGradient>
        <linearGradient id="site-view" x1="0" y1="0" x2="0" y2="1">
          <stop offset="0" stop-color="#6fa2da"/>
          <stop offset=".6" stop-color="#2f5fb8"/>
          <stop offset="1" stop-color="#5a5d66"/>
        </linearGradient>
        <linearGradient id="tint-navy" x1="0" y1="0" x2="1" y2="1">
          <stop offset="0" stop-color="#2a3d98"/>
          <stop offset="1" stop-color="#1b2672"/>
        </linearGradient>
        <linearGradient id="residential-tower" x1="0" y1="0" x2="0" y2="1">
          <stop offset="0" stop-color="#c9c6c0"/>
          <stop offset=".7" stop-color="#9b8a76"/>
          <stop offset="1" stop-color="#6f7a6a"/>
        </linearGradient>
        <linearGradient id="office-tower" x1="0" y1="0" x2="1" y2="1">
          <stop offset="0" stop-color="#a9bfd8"/>
          <stop offset=".6" stop-color="#7890ae"/>
          <stop offset="1" stop-color="#a9aeb4"/>
        </linearGradient>
      </defs>

      <!-- left page imagery -->
      <polygon role="img" aria-label="Photo of a glass curtain wall office building against a blue sky" fill="url(#glass-tower)" points="160,0 400,0 400,155 160,222"/>
      <polygon role="img" aria-label="Photo of an installer guiding a unitized glass panel into place on a high-rise floor" fill="url(#site-view)" points="235,212 400,176 400,455 235,492"/>
      <polygon role="img" aria-label="Navy-tinted photo of a glass building facade" fill="url(#tint-navy)" points="235,505 400,468 400,563 232,563"/>

      <!-- left page bands -->
      <polygon fill="var(--grey)" points="0,266 400,162 400,178 0,283"/>
      <line x1="20" y1="257" x2="160" y2="219" stroke="var(--grey)" stroke-width="4"/>
      <line x1="110" y1="250" x2="233" y2="218" stroke="var(--grey)" stroke-width="4"/>
      <polygon fill="var(--navy-deep)" points="0,546 400,443 400,461 0,563"/>
      <line x1="18" y1="527" x2="232" y2="472" stroke="var(--navy-deep)" stroke-width="4"/>

      <!-- right page imagery -->
      <polygon role="img" aria-label="Photo of a residential high-rise tower with a street-level podium" fill="url(#residential-tower)" points="590,0 800,0 800,278 590,225"/>
      <polygon role="img" aria-label="Photo of a tall blue glass office tower" fill="url(#office-tower)" points="590,262 800,320 800,563 762,563 590,512"/>
      <polygon role="img" aria-label="Photo of a street-level building base" fill="#9a9c9f" points="400,478 705,563 400,563"/>

      <!-- right page bands -->
      <polygon fill="var(--grey)" points="400,181 800,292 800,308 400,198"/>
      <line x1="445" y1="184" x2="585" y2="221" stroke="var(--grey)" stroke-width="4"/>
      <line x1="523" y1="240" x2="590" y2="258" stroke="var(--navy-deep)" stroke-width="4"/>
      <rect x="590" y="258" width="5" height="254" fill="var(--navy-deep)"/>
      <polygon fill="var(--navy-deep)" points="400,452 765,563 722,563 400,470"/>
      <line x1="478" y1="463" x2="590" y2="493" stroke="var(--navy-deep)" stroke-width="4"/>
    </svg>
    <div class="fold"></div>

    <!-- left page -->
    <div class="brand-name">KT Hollin's</div>
    <h1 class="display-title title-left">Panelform<br>Systems</h1>
    <ul class="product-list">
      <li>Curtain Wall</li>
      <li>Window Wall</li>
      <li>Ribbon Window</li>
      <li>Storefront</li>
    </ul>
    <p class="lead-copy">Unitzed products can be<br>installed in one third of the<br>time with one third of the<br>installers versus<br>traditonal stck products.</p>
    <ul class="benefit-list">
      <li>Enclose a building faster allowing other trades to start earlier</li>
      <li>Less installers required</li>
      <li>Manufacturing done in a controlled environment</li>
      <li>Standard work and quality control inspectons</li>
    </ul>

    <!-- right page -->
    <h2 class="display-title title-right">Unitized<br>Curtain Wall</h2>
    <p class="intro-copy">Designed by installers for Installers with quality and efficient Installaton. Complete up to 40 panels a day with one installaton team.</p>
    <ul class="feature-list">
      <li>Industry<br>leading 2 1/2”<br>overall adjustment for out of tolerance structures</li>
      <li>Alignment pins allow for 1/4” forgiveness to engage units</li>
      <li>Trim clips and anchors are attached</li>
      <li>Shipped on metal racks or wood crates</li>
    </ul>
  </div>
</body>
</html>
```